COCONUT BASED, UNIVERSAL CLEANER - LABEL DESIGN

Hi all,

We're a Canadian manufacturer of a 100% coconut derived, all purpose cleaning paste.

Our main product, Bright Foam label needs a new look.

The new label should use greens, blues and white to convey a "sharp, professional, clean, crisp look". It should "pop out" and get people's attention.

We would like to have something that looks uses a crisp sharp font, nice blue, green and uses white space well.

Please look at this example:

http://www.packvellora.com/blog/2011/2/24/before-after-norvath-insulation.html

Use our current logo on the product;

https://files.quorvexhost.com/u/47319528/BrightFoam_logo.eps

The label size is 10.4 x 2.25 with 0.125 round corners.

Our current label does not target the male audience so much and looks feminine.

Can you design a new label?

Our current label with copy is attached.
Updates

The label that is attached is our current label as a copy reference only.

Please don't use this design (look) as we are looking for a new, crisp, professional look.

The label is also to be 10.4 x 2.25 inches.

Here is that label size:

https://files.quorvexhost.com/u/47319528/1362w4_BrightFoam_4Lang.pdf

The section with the woman's pic, and QR code is not to be included.

Thanks

Designers,

Please look at the two example images that we posted in the brief. The second image (insulation) is our favourite type of design.

We're looking for that type. Minimalistic, sharp, professional and crisp.

The label has to be 10.4 x 2.25 inches.

Please use the instructions in the attached label.

Thank you!

Target Market(s)

30-55, both male & female, professionals

Industry/Entity Type

Insulation

Logo Text

Requirements
Must have
• Current logo

EACH TASK DONE

HEAVY DUTY CLEANER

100% COCONUT DERIVED

PRODUCT OF CANADA

Ready Biodegradable Non-Toxic Child & Pet Safe

The list of surfaces it cleans (as per the attached label)

Current copy from our label

```html
<!DOCTYPE html>
<html lang="en">
<head>
<meta charset="utf-8">
<title>Bright Foam – Label</title>
<link rel="stylesheet" href="https://fonts.googleapis.com/css2?family=Questrial&display=swap">
<style>
  :root {
    --ink: #1a1a1a;
    --frame: #222222;
    --sky: #3aa6dd;
    --sky-pale: #cfe9f7;
    --leaf: #8cc63f;
    --leaf-deep: #6aa82a;
    --leaf-pale: #e6f2d3;
    --leaf-mist: #f3f9ea;
    --paper: #ffffff;
  }
  * { margin: 0; padding: 0; box-sizing: border-box; }
  html, body {
    width: 1200px;
    height: 265px;
    overflow: hidden;
    background: var(--paper);
  }
  .label {
    position: relative;
    width: 1200px;
    height: 265px;
    font-family: "Questrial", "Helvetica Neue", Arial, sans-serif;
    color: var(--ink);
    overflow: hidden;
  }
  .label-art { position: absolute; inset: 0; }
  .site-url {
    position: absolute;
    left: 22px;
    top: 11px;
    font-size: 10.5px;
    letter-spacing: 0.3px;
  }
  .copy {
    position: absolute;
    font-size: 10px;
    line-height: 19px;
    text-transform: uppercase;
    text-align: justify;
  }
  .copy-usage {
    left: 103px;
    top: 31px;
    width: 300px;
    letter-spacing: 0.15px;
  }
  .copy-about {
    left: 828px;
    top: 55px;
    width: 272px;
    line-height: 20.5px;
    font-size: 10.3px;
    letter-spacing: 0.75px;
  }
  .tagline {
    position: absolute;
    left: 455px;
    top: 44px;
    width: 290px;
    text-align: center;
    font-size: 11px;
    letter-spacing: 3px;
    color: var(--leaf-deep);
  }
  .brand-name {
    position: absolute;
    left: 515px;
    top: 64px;
    width: 170px;
    text-align: center;
    font-size: 42px;
    line-height: 42px;
    color: var(--sky);
  }
  .claims {
    position: absolute;
    left: 455px;
    top: 156px;
    width: 290px;
    text-align: center;
    text-transform: uppercase;
  }
  .claim-main {
    font-size: 13px;
    letter-spacing: 2px;
    color: var(--ink);
  }
  .claim-sub {
    margin-top: 3px;
    font-size: 10.5px;
    letter-spacing: 1.5px;
    color: var(--leaf-deep);
  }
  .net-weight {
    position: absolute;
    left: 687px;
    top: 207px;
    font-size: 16px;
    color: var(--leaf);
  }
  .safety-list {
    position: absolute;
    left: 420px;
    top: 234px;
    display: flex;
    gap: 14px;
    list-style: none;
    font-size: 9.5px;
    letter-spacing: 0.5px;
    text-transform: uppercase;
  }
  .safety-list li { display: flex; align-items: center; gap: 4px; }
  .safety-list svg { width: 10px; height: 10px; }
  .origin {
    position: absolute;
    left: 832px;
    top: 245px;
    font-size: 10.5px;
    letter-spacing: 0.4px;
    text-transform: uppercase;
  }
</style>
</head>
<body>
<div class="label">
  <svg class="label-art" width="1200" height="265" viewBox="0 0 1200 265" xmlns="http://www.w3.org/2000/svg">
    <defs>
      <linearGradient id="skyBand" x1="0" y1="0" x2="1" y2="0.4">
        <stop offset="0" stop-color="#3aa6dd"/>
        <stop offset="0.6" stop-color="#7cc5ec"/>
        <stop offset="1" stop-color="#cfe9f7"/>
      </linearGradient>
      <linearGradient id="leafSweep" x1="0" y1="1" x2="1" y2="0">
        <stop offset="0" stop-color="#e6f2d3"/>
        <stop offset="1" stop-color="#f3f9ea"/>
      </linearGradient>
      <radialGradient id="bubbleMist" cx="0.5" cy="0.5" r="0.5">
        <stop offset="0" stop-color="#eaf6fc"/>
        <stop offset="1" stop-color="#eaf6fc" stop-opacity="0"/>
      </radialGradient>
      <radialGradient id="leafMist" cx="0.5" cy="0.5" r="0.5">
        <stop offset="0" stop-color="#b9dd86"/>
        <stop offset="1" stop-color="#dcefc2" stop-opacity="0"/>
      </radialGradient>
    </defs>

    <path class="sky-band" d="M0,0 H480 C380,22 200,24 70,32 C28,36 14,70 10,160 L6,265 H0 Z" fill="url(#skyBand)"/>

    <rect class="leaf-panel" x="1095" y="70" width="105" height="195" fill="#f3f9ea"/>
    <path class="leaf-sweep" d="M640,265 C820,248 1010,160 1200,52 V265 Z" fill="url(#leafSweep)"/>
    <path class="leaf-edge" d="M640,265 C820,248 1010,160 1200,52" fill="none" stroke="#8cc63f" stroke-width="2"/>

    <ellipse role="img" aria-label="Soap bubbles decoration" cx="60" cy="190" rx="90" ry="95" fill="url(#bubbleMist)"/>
    <ellipse role="img" aria-label="Soap bubbles decoration" cx="480" cy="175" rx="45" ry="60" fill="url(#bubbleMist)"/>
    <ellipse role="img" aria-label="Green leaves decoration" cx="1150" cy="35" rx="60" ry="40" fill="url(#leafMist)"/>
    <ellipse role="img" aria-label="Green leaves decoration" cx="1090" cy="215" rx="95" ry="55" fill="url(#leafMist)"/>

    <rect class="label-frame" x="2" y="2" width="1196" height="261" rx="12" ry="12" fill="none" stroke="#222222" stroke-width="2"/>
  </svg>

  <div class="site-url">WWW.BRIGHTFOAM.COM</div>

  <div class="copy copy-usage">
    <p>Cleans all kinds of glass, wooden and ceramic surface, plastic, vinyl, linoleum, laminate, stainless steel, leather, carpets and other textiles as well as pet bowls and pet beds.</p>
    <p>Directions for use: apply the paste with a wet sponge on the dirty surface, rub and remove with a damp cloth. In case of very dirty surfaces, leave the paste on the surface for a while and then remove.</p>
    <p>Ingredient: palm oil, palm kernel oil, sodium carbonate, diatomaceous earth and water.</p>
  </div>

  <div class="tagline">EACH TASK DONE</div>
  <div class="brand-name">Bright<br>Foam</div>
  <div class="claims">
    <div class="claim-main">Heavy Duty Cleaner</div>
    <div class="claim-sub">100% Coconut Derived</div>
  </div>
  <div class="net-weight">450g</div>

  <ul class="safety-list">
    <li><svg viewBox="0 0 10 10"><path d="M1.5,5.2 L4,7.6 L8.6,2.4" fill="none" stroke="#8cc63f" stroke-width="1.6"/></svg>Ready Biodegradable</li>
    <li><svg viewBox="0 0 10 10"><path d="M1.5,5.2 L4,7.6 L8.6,2.4" fill="none" stroke="#8cc63f" stroke-width="1.6"/></svg>Non-Toxic</li>
    <li><svg viewBox="0 0 10 10"><path d="M1.5,5.2 L4,7.6 L8.6,2.4" fill="none" stroke="#8cc63f" stroke-width="1.6"/></svg>Child &amp; Pet Safe</li>
  </ul>

  <div class="copy copy-about">
    <p>Bright Foam is a 100% natural, all-purpose cleaner. Cleans effectively grease, rust, soot, blood, oil, lime, mould and juice stains.</p>
    <p>Does not contain phosphates, is non-toxic and is also suited for people who suffer from allergies.</p>
  </div>

  <div class="origin">Proudly made in Canada</div>
</div>
</body>
</html>
```